Need a cover for eBook:
Title is: 41 Blunders That Sink Your Indie-Released Volume.
Remarks about the title: I know that is difficult to design a cover with a number. You can add the word TOP (in caps or not) before 41 blunders. It is not mandatory to insert the word TOP. It is up to you if you think you can create a better cover.
Subtitle is: A Newcomer's Manual for Releasing Solo, Arranging Pictures and Words, Planning Pages, Boosting Sign-ups and Moving More Copies
Author: Dennis R. Walbrey
Publisher: Quillmark Press
The book made the presentation of errors that can occur during the production of an ebook. Title must be big, the title should be readable even when the image is reduced in size. No photo please.
I join my projects as an example. Do what you want but I need impact.

Target Market(s)

Book to sell first at Brimfold Reader Shop. Target is authors, men or women, who want to produce ebooks.

Industry/Entity Type

Publishing Company

Font styles to use
Sans Serif

Colors
3176b5
9bcb3c

Requirements
Must have
• High readability when cover is small.
• Here is the definition of the word KILL
• put an end to or cause the failure or defeat of (something).
• "the committee voted to kill the project"
• synonyms: destroy, put an end to, end, extinguish, dash, quash, ruin, wreck, shatter, smash, crush, scotch, thwart; informalput the kibosh on, stymie, scuttle
• "this would kill all hopes of progress"
• veto, defeat, vote down, rule against, reject, throw out, overrule, overturn, put a stop to, quash, squash
• "an opposition attempt to kill the bill"
Nice to have
• I suggested 2 colors but you can you use another one or two. I want cover that sell. There is so bright ideas here. Come on down!
Should not have
• No picture or photo. If a photo or an object had power to the cover, you can insert one. I don't want a photo-collage.

```html
<!DOCTYPE html>
<html lang="en">
<head>
<meta charset="utf-8">
<title>41 Blunders That Sink Your Indie-Released Volume — Cover</title>
<link rel="stylesheet" href="https://fonts.googleapis.com/css2?family=Baloo+2:wght@700;800&family=Righteous&family=Zilla+Slab:wght@700&display=swap">
<style>
  :root {
    --stage-light: #e6e6e6;
    --stage-dark: #a9a9a9;
    --green-light: #a9d352;
    --green: #9bcb3c;
    --green-deep: #8bbd2c;
    --blue: #3176b5;
    --blue-light: #4a8cc7;
    --number-outline: #ffffff;
    --white: #ffffff;
    --pencil-wood: #e9d7a6;
    --pencil-wood-shade: #d9c48c;
    --pencil-stripe: #2c3f78;
    --pencil-tip: #f08a3c;
  }
  * { margin: 0; padding: 0; box-sizing: border-box; }
  html, body { width: 1200px; height: 1200px; overflow: hidden; }
  body {
    background: radial-gradient(circle at 50% 45%, var(--stage-light) 0%, var(--stage-dark) 100%);
    position: relative;
  }
  .visually-hidden {
    position: absolute; width: 1px; height: 1px; overflow: hidden; clip: rect(0 0 0 0); white-space: nowrap;
  }
  .cover {
    position: absolute;
    left: 200px; top: 120px;
    width: 800px; height: 960px;
    background: linear-gradient(180deg, var(--green-light) 0%, var(--green) 55%, var(--green-deep) 100%);
    overflow: hidden;
  }
  .author {
    position: absolute; top: 52px; left: 0; width: 100%;
    text-align: center;
    font-family: "Baloo 2", sans-serif; font-weight: 700;
    font-size: 40px; color: var(--white); letter-spacing: 0.5px;
  }
  .title { position: absolute; inset: 0; }
  .title-number {
    position: absolute; left: 34px; top: 140px;
    font-family: "Righteous", sans-serif;
    font-size: 280px; line-height: 1; letter-spacing: -6px;
    color: var(--blue);
    -webkit-text-stroke: 6px var(--number-outline);
    paint-order: stroke fill;
  }
  .title-word {
    position: absolute; left: 318px; top: 176px;
    font-family: "Zilla Slab", serif; font-weight: 700;
    font-size: 112px; line-height: 0.88; color: var(--white);
    text-transform: uppercase;
  }
  .title-line {
    position: absolute; left: 20px; width: 660px; top: 398px;
    text-align: center; white-space: nowrap;
    font-family: "Zilla Slab", serif; font-weight: 700;
    font-size: 80px; line-height: 1; color: var(--white);
    text-transform: uppercase;
  }
  .title-tail {
    position: absolute; left: 20px; width: 660px; top: 492px;
    text-align: center; white-space: nowrap;
    font-family: "Righteous", sans-serif;
    font-size: 42px; line-height: 1.1; color: var(--blue);
    text-transform: uppercase;
  }
  .pencil-area { position: absolute; display: block; }
  .pencil-horizontal { left: 0; top: 572px; width: 720px; height: 68px; }
  .pencil-vertical { left: 706px; top: 150px; width: 60px; height: 470px; }
  .info-band {
    position: absolute; left: 0; top: 640px; width: 800px; height: 320px;
    background: linear-gradient(180deg, var(--blue-light) 0%, var(--blue) 100%);
  }
  .subtitle {
    position: absolute; top: 40px; left: 60px; right: 60px;
    text-align: center;
    font-family: "Baloo 2", sans-serif; font-weight: 800;
    font-size: 24px; line-height: 1.2; color: var(--white);
  }
  .publisher {
    position: absolute; top: 160px; left: 0; width: 100%;
    text-align: center;
    font-family: "Baloo 2", sans-serif; font-weight: 800;
    font-size: 26px; color: var(--white);
  }
</style>
</head>
<body>
  <main class="cover">
    <p class="author">Dennis R. Walbrey</p>

    <svg class="pencil-area pencil-vertical" role="img" aria-label="Illustration of an upright striped pencil with an orange eraser" viewBox="0 0 60 470" preserveAspectRatio="none">
      <defs>
        <linearGradient id="wood-vertical" x1="0" y1="0" x2="1" y2="0">
          <stop offset="0" stop-color="var(--pencil-wood)"/>
          <stop offset="1" stop-color="var(--pencil-wood-shade)"/>
        </linearGradient>
      </defs>
      <rect x="0" y="0" width="60" height="470" rx="6" fill="url(#wood-vertical)"/>
    </svg>
    <svg class="pencil-area pencil-horizontal" role="img" aria-label="Illustration of a sharpened striped pencil lying across the cover" viewBox="0 0 720 68" preserveAspectRatio="none">
      <defs>
        <linearGradient id="wood-horizontal" x1="0" y1="0" x2="0" y2="1">
          <stop offset="0" stop-color="var(--pencil-wood)"/>
          <stop offset="1" stop-color="var(--pencil-wood-shade)"/>
        </linearGradient>
      </defs>
      <rect x="0" y="0" width="720" height="68" fill="url(#wood-horizontal)"/>
    </svg>

    <h1 class="title">
      <span class="visually-hidden">41 Blunders That Sink Your Indie-Released Volume</span>
      <span class="title-number" aria-hidden="true">41</span>
      <span class="title-word" aria-hidden="true">Blun<br>ders</span>
      <span class="title-line" aria-hidden="true">That Sink Your</span>
      <span class="title-tail" aria-hidden="true">Indie-Released Volume</span>
    </h1>

    <section class="info-band">
      <p class="subtitle">A Newcomer's Manual for Releasing Solo, Arranging Pictures and Words, Planning Pages, Boosting Sign-ups and Moving More Copies</p>
      <p class="publisher">Quillmark Press</p>
    </section>
  </main>
</body>
</html>
```